Bright Arch Group business card

Bright Arch Group is the parent company of Bright Arch Building, Bright Arch Plumbing and Bright Arch Renovating. We require a sophisticated business card that covers all aspects of the building and plumbing space without using told or construction items.

Industry/Entity Type

Construction Company

Contact Information for Business Card

Gareth Pimley
Director
0472915083
gareth@brightarch.com.au
Www.brightarch.com.au

Font styles to use
Serif
Sans Serif

Colors
3176b5
ffce3e
0692cd
34a7d8
fbee3e
faa54b

Requirements
Must have
• Logo on front
• Logo and details on rear.
Nice to have
• Maybe water mark or shadow effect with logo
Should not have
• Tools or any construction associated items

```html
<!DOCTYPE html>
<html lang="en">
<head>
<meta charset="UTF-8">
<title>Bright Arch Group – Business Card</title>
<link href="https://fonts.googleapis.com/css2?family=Montserrat:wght@300;400;500&display=swap" rel="stylesheet">
<style>
  :root {
    --backdrop: #e6e7e8;
    --card: #000000;
    --accent: #f7861e;
    --ink: #ffffff;
  }
  * { margin: 0; padding: 0; box-sizing: border-box; }
  html, body {
    width: 1200px; height: 927px; overflow: hidden;
    background: var(--backdrop);
    font-family: "Montserrat", sans-serif;
  }
  .stage { position: relative; width: 1200px; height: 927px; }
  .card {
    position: absolute; top: 111px;
    width: 403px; height: 705px;
    background: var(--card);
    color: var(--ink);
    text-align: center;
  }
  .card--front { left: 180px; }
  .card--back { left: 617px; }

  .brand {
    position: absolute; left: 0; right: 0; top: 200px;
    font-weight: 300; color: var(--ink);
    text-transform: uppercase;
  }
  .brand__name { font-size: 38px; letter-spacing: 10px; line-height: 1.1; padding-left: 10px; }
  .brand__sub { font-size: 24px; letter-spacing: 17px; margin-top: 4px; padding-left: 17px; }

  .person { position: absolute; left: 0; right: 0; top: 392px; }
  .person__name { font-size: 27px; font-weight: 500; color: var(--accent); }
  .person__role { font-size: 17px; font-weight: 400; margin-top: 2px; }

  .icons {
    position: absolute; left: 0; right: 0; top: 464px;
    display: flex; justify-content: center; gap: 8px;
  }
  .icons svg { width: 12px; height: 12px; }

  .contact { position: absolute; left: 0; right: 0; top: 494px; font-size: 18px; font-weight: 400; line-height: 25px; }
  .contact__highlight { color: var(--accent); font-weight: 500; }

  .back-brand {
    position: absolute; left: 0; right: 0; top: 322px;
    font-weight: 300; color: var(--accent);
    font-size: 40px; letter-spacing: 8px; text-transform: uppercase; line-height: 1.2;
    padding-left: 8px;
  }
</style>
</head>
<body>
<main class="stage">
  <section class="card card--front">
    <div class="brand">
      <div class="brand__name">Bright Arch</div>
      <div class="brand__sub">Group</div>
    </div>

    <div class="person">
      <div class="person__name">Gareth Pimley</div>
      <div class="person__role">Director</div>
    </div>

    <div class="icons" aria-hidden="true">
      <svg viewBox="0 0 12 12" fill="none" stroke="#f7861e" stroke-width="1.2" stroke-linecap="round" stroke-linejoin="round">
        <path d="M2.5 1.5 L4.3 1.5 L5 4 L3.8 5 Q5 7.5 7 8.2 L8 7 L10.5 7.7 L10.5 9.5 Q10 10.8 8.5 10.5 Q3.5 9 1.5 3.5 Q1.3 2 2.5 1.5 Z"/>
      </svg>
      <svg viewBox="0 0 12 12" fill="none" stroke="#f7861e" stroke-width="1.2" stroke-linejoin="round">
        <rect x="1" y="2.5" width="10" height="7"/>
        <path d="M1 2.5 L6 6.5 L11 2.5"/>
      </svg>
      <svg viewBox="0 0 12 12" fill="none" stroke="#f7861e" stroke-width="1">
        <circle cx="6" cy="6" r="5"/>
        <ellipse cx="6" cy="6" rx="2.2" ry="5"/>
        <path d="M1 6 H11 M2 3.5 H10 M2 8.5 H10"/>
      </svg>
    </div>

    <div class="contact">
      <div class="contact__phone">0472915083</div>
      <div class="contact__email">gareth@brightarch.com.au</div>
      <div class="contact__web">www.<span class="contact__highlight">brightarch</span>.com.au</div>
    </div>
  </section>

  <section class="card card--back">
    <div class="back-brand">Bright Arch<br>Group</div>
  </section>
</main>
</body>
</html>
```